名刺の背景は、白地(裏地デザインは、ありもOK)
複数の色味というよりは、シンプルな色使い

シンプルだけど、上品さを感じるもの

株式会社plumeridge/代表取締役/名前/読みがな(英語)/住所/電話番号/mail address/HP URL
シンプル 複雑
単色 カラフル
暗い 明るい
日常 高級
遊び心 厳粛
未来的 伝統的
女性的 男性的
緑系、グレー系、色は絶対ではありませんので、イメージやデザインに添ってご提案いただけるのであれば嬉しいです
• 高解像度JPG (.jpg)
• イラストレーター形式 (.ai)
• フォトショップ形式 (.psd)
• PNG形式 (.png)
現在の色味が、添付ファイルの名刺の色なので、参考にしていただけると嬉しいです。
緑というよりは、エメラルドグリーンのような色味です。
※添付ファイルに記載されている、個人情報は名刺サンプルに記載しないでください。
お手数ですがよろしくお願いいたします。
※社名は「株式会社plumeridge」のみで、「inc.」は無しでお願いいたします。
たくさんのご提案ありがとうございます!
デザインが一般企業よりのものを探しており、可能であれば、
もう少しデザインを拝見したく、延長させていただきました。

お忙しいところお手数ですが、どうぞよろしくお願いいたします。

デザイン性が一番高かったためです。

たくさんのご提案、ありがとうございました!
ご丁寧にご対応いただき、とても助かりました。
また依頼あれば出させていただきます。

```html
<!DOCTYPE html>
<html lang="ja">
<head>
<meta charset="utf-8">
<title>plumeridge 名刺</title>
<link rel="stylesheet" href="https://fonts.googleapis.com/css2?family=Noto+Sans+JP:wght@400;500;700&display=swap">
<style>
  :root {
    --emerald: #1c9d8f;
    --emerald-soft: #5dbdb2;
    --ink: #333333;
    --muted: #666666;
    --paper: #ffffff;
    --page: #ffffff;
    --shadow: rgba(0, 0, 0, 0.35);
  }
  * { box-sizing: border-box; margin: 0; padding: 0; }
  html, body {
    width: 871px; height: 1200px; overflow: hidden;
    background: var(--page);
    font-family: "Noto Sans JP", sans-serif;
    color: var(--ink);
  }
  .card {
    position: absolute;
    left: 29px; width: 813px;
    box-shadow: 8px 10px 14px var(--shadow);
  }
  .card-front { top: 23px; height: 557px; background: var(--paper); }
  .card-back { top: 645px; height: 502px; background: var(--emerald); }

  .brand {
    position: absolute; left: 60px; top: 90px;
    display: flex; align-items: center; gap: 14px;
  }
  .brand-dot { width: 46px; height: 46px; border-radius: 50%; background: var(--emerald); }
  .brand-name {
    font-size: 50px; font-weight: 400; letter-spacing: 3px;
    color: var(--emerald); line-height: 1;
  }

  .person { position: absolute; left: 58px; top: 200px; }
  .person-title { font-size: 17px; color: var(--muted); }
  .person-name { margin-top: 6px; font-size: 36px; font-weight: 700; letter-spacing: 6px; }
  .person-reading { font-size: 14px; font-weight: 400; letter-spacing: 0; color: var(--muted); margin-left: 8px; }

  .company { position: absolute; left: 415px; top: 340px; font-size: 22px; font-weight: 500; }
  .contact { position: absolute; left: 415px; top: 382px; list-style: none; }
  .contact li { display: flex; align-items: center; gap: 10px; height: 34.5px; font-size: 19px; }
  .contact-icon {
    width: 22px; height: 22px; border-radius: 50%; background: var(--emerald);
    display: flex; align-items: center; justify-content: center; flex: none;
  }
  .postal { position: absolute; left: 255px; top: 520px; font-size: 19px; }
  .address { position: absolute; left: 415px; top: 520px; font-size: 19px; }

  .back-mark {
    position: absolute; left: 361px; top: 216px;
    width: 90px; height: 90px; border-radius: 50%; background: var(--emerald-soft);
  }
  .back-url {
    position: absolute; left: 0; right: 0; top: 440px; text-align: center;
    color: var(--paper); font-size: 22px; font-weight: 700; letter-spacing: 3px;
  }
</style>
</head>
<body>
  <section class="card card-front">
    <div class="brand">
      <span class="brand-dot"></span>
      <span class="brand-name">plumeridge</span>
    </div>
    <div class="person">
      <p class="person-title">代表取締役</p>
      <p class="person-name">佐藤 美咲<span class="person-reading">Sato Misaki</span></p>
    </div>
    <p class="company">株式会社 plumeridge</p>
    <ul class="contact">
      <li>
        <span class="contact-icon"><svg width="12" height="12" viewBox="0 0 12 12"><path d="M2.5 1.5h2l1 2.5-1.3.9a6 6 0 0 0 2.9 2.9l.9-1.3 2.5 1v2a1 1 0 0 1-1 1A9 9 0 0 1 1.5 2.5a1 1 0 0 1 1-1z" fill="#fff"/></svg></span>
        <span>03 5550 2187</span>
      </li>
      <li>
        <span class="contact-icon"><svg width="12" height="12" viewBox="0 0 12 12"><rect x="2" y="1.5" width="8" height="9" fill="none" stroke="#fff" stroke-width="1.4"/><line x1="4" y1="4.5" x2="8" y2="4.5" stroke="#fff"/><line x1="4" y1="7" x2="8" y2="7" stroke="#fff"/></svg></span>
        <span>03 5550 2188</span>
      </li>
      <li>
        <span class="contact-icon"><svg width="12" height="12" viewBox="0 0 12 12"><rect x="1" y="2.5" width="10" height="7" fill="none" stroke="#fff" stroke-width="1.3"/><path d="M1 2.5l5 4 5-4" fill="none" stroke="#fff" stroke-width="1.3"/></svg></span>
        <span>info@plumeridge.co.jp</span>
      </li>
      <li>
        <span class="contact-icon"><svg width="12" height="12" viewBox="0 0 12 12"><circle cx="6" cy="6" r="4.5" fill="none" stroke="#fff" stroke-width="1.2"/><ellipse cx="6" cy="6" rx="2" ry="4.5" fill="none" stroke="#fff"/><line x1="1.5" y1="6" x2="10.5" y2="6" stroke="#fff"/></svg></span>
        <span>www.plumeridge.co.jp</span>
      </li>
    </ul>
    <p class="postal">〒 107-0062</p>
    <p class="address">東京都港区赤坂 9-8-76</p>
  </section>

  <section class="card card-back">
    <span class="back-mark"></span>
    <p class="back-url">www.plumeridge.co.jp</p>
  </section>
</body>
</html>
```